"The Plum Principle" Book Cover Design

Name of book: The Plum Principle

Tagline: Exploring 8 essential truths to living and loving more deeply.

Author: Rosalinda Paredes-Oquendo

Size: 5in w x 8in h Paperback

This is the second book of 30 year old Entrepreneur, Author and Speaker. The book basically tells the story of her youth and immigrating to the United States at 14.

"The Plum Principle" name came about since she started selling figs outside her home in mexico city... Her family had a fig three in their backyard, and when she was about 6 she had the courage of starting her own business.

Here is the Book Description:
At some point in our lives, we all face the question: Does crisis and pain propel us forward or put our lives on hold? In this deeply intimate memoir, Rosalinda Paredes Oquendo shares the eight hidden secrets—the fig factors as she calls them—of discovering true awareness and embracing life’s big sky possibilities, even amidst our greatest struggles.

The Plum Principle is an emotionally-charged story spanning two countries and three decades. Oquendo expertly takes our hand and invites us to walk with her. We begin in her homeland of Mexico as she recounts her mother’s unrelenting faith in giving birth to a little girl, the good that came from the arsonist’s flames devouring her childhood home and the life-changing discovery she encountered after watching her father walk away again and again with a bottle in his hand. Her immigration to the United States as a young teenager and the amazing medical discovery that both saved her life while nearly taking it away offer true inspiration that the human spirit dictates triumph in the lives of everyday people.

Oquendo clearly touches our hearts in this beautifully written, very personal memoir, showing us how to find more to every moment of living through love, awareness, forgiveness, gratitude and more. Each chapter is capped off with thought-provoking questions underscoring Oquendo’ real message: the answers to life’s greatest questions lie within each of us.
Updates

The author's favorite colors are Purple, Lime Green, and Black...  notice that Figs are also purple

Target Market(s)

Mostly women but men should also get interested in reading book

Industry/Entity Type

Medical

Requirements
Must have
• Title, tagline, and author's name;

The Plum Principle

Exploring the 8 essential truths to living and loving more deeply

Rosalinda Paredes-Oquendo

```html
<!DOCTYPE html>
<html lang="en">
<head>
<meta charset="utf-8">
<title>The Plum Principle — Book Cover</title>
<link rel="stylesheet" href="https://fonts.googleapis.com/css2?family=Bebas+Neue&family=Julius+Sans+One&display=swap">
<style>
  :root {
    --plum-band: #5a2e42;
    --paper: #ffffff;
    --author-grey: #bdbdbd;
    --tagline-grey: #a9a9a9;
    --title-ink: #0b0b0b;
    --fruit-deep: #7d3a6c;
    --fruit-flesh: #c9646f;
  }
  * { margin: 0; padding: 0; box-sizing: border-box; }
  html, body { width: 750px; height: 1200px; overflow: hidden; background: var(--paper); }
  .cover {
    position: relative;
    width: 750px;
    height: 1200px;
    background: var(--paper);
    overflow: hidden;
  }
  .band { position: absolute; left: 0; width: 100%; background: var(--plum-band); }
  .band--top { top: 0; height: 68px; }
  .band--upper-title { top: 913px; height: 59px; }
  .band--bottom { top: 1063px; height: 137px; }

  .author {
    position: absolute;
    left: 46px;
    top: 92px;
    font-family: "Julius Sans One", sans-serif;
    font-weight: 400;
    font-size: 64px;
    line-height: 82px;
    letter-spacing: 0.36em;
    color: var(--author-grey);
    text-transform: uppercase;
  }
  .author span { display: block; }

  .fruit-photo {
    position: absolute;
    left: 185px;
    top: 380px;
    width: 372px;
    height: 345px;
    background: radial-gradient(ellipse at 50% 50%, var(--fruit-flesh) 0%, var(--fruit-deep) 45%, rgba(125, 58, 108, 0) 72%);
  }

  .tagline {
    position: absolute;
    left: 0;
    top: 758px;
    width: 722px;
    text-align: center;
    font-family: "Bebas Neue", sans-serif;
    font-size: 23px;
    line-height: 38px;
    letter-spacing: 0.2em;
    color: var(--tagline-grey);
    text-transform: uppercase;
  }

  .title {
    position: absolute;
    left: 0;
    top: 972px;
    width: 750px;
    height: 91px;
    display: flex;
    align-items: center;
    justify-content: center;
    font-family: "Bebas Neue", sans-serif;
    font-size: 66px;
    font-weight: 400;
    letter-spacing: 0.17em;
    padding-left: 0.17em;
    color: var(--title-ink);
    text-transform: uppercase;
  }
</style>
</head>
<body>
  <main class="cover">
    <div class="band band--top"></div>

    <h2 class="author">
      <span>Rosalinda</span>
      <span>Paredes-</span>
      <span>Oquendo</span>
    </h2>

    <div class="fruit-photo" role="img" aria-label="Photograph of a whole purple fruit beside a halved one showing its red seeded flesh"></div>

    <p class="tagline">Exploring 8 essential truths<br>to living and loving more deeply.</p>

    <div class="band band--upper-title"></div>
    <h1 class="title">The Plum Principle</h1>
    <div class="band band--bottom"></div>
  </main>
</body>
</html>
```